Wattlegrove Campus Lodgings needs a business card design

Hi Guys,

We are a Student Accommodation company in Australia. We already have a logo which I will submit.

I will require the design of the business cards from you.

I am after something that looks clean, modern and that people feel interested and actually want to contact us.

We would like to see designs that are innovative.

On the business cards I will require to have:

Employee Name
Position
Phone number
Email
Facebook page

I hope you can help me with this project guys as I have heard really good things from you.

```html
<!DOCTYPE html>
<html lang="en">
<head>
<meta charset="utf-8">
<title>Wattlegrove Campus Lodgings – Business Card</title>
<link rel="stylesheet" href="https://fonts.googleapis.com/css2?family=PT+Sans:wght@400;700&family=PT+Sans+Narrow:wght@400;700&display=swap">
<style>
  :root {
    --backdrop: #1eae9a;
    --card: #ffffff;
    --green: #0b8b47;
    --yellow: #fbbf33;
    --ink: #231f20;
    --muted: #7a7a7a;
    --faint-yellow: #fdf3e0;
    --faint-green: #e8eee6;
  }
  * { margin: 0; padding: 0; box-sizing: border-box; }
  html, body { width: 1200px; height: 720px; overflow: hidden; }
  body {
    background: var(--backdrop);
    position: relative;
    font-family: "PT Sans Narrow", "Arial Narrow", sans-serif;
  }
  .card {
    position: absolute;
    top: 234px;
    width: 444px;
    height: 240px;
    background: var(--card);
    overflow: hidden;
  }
  .card--front { left: 133px; }
  .card--back { left: 623px; width: 441px; }

  .backdrop-shape {
    position: absolute;
    background: linear-gradient(180deg, var(--faint-yellow), var(--faint-green));
  }
  .card--front .backdrop-shape { right: 0; top: 20px; width: 110px; height: 220px; }
  .card--back .backdrop-shape { left: 30px; top: 0; width: 180px; height: 240px; }

  .brand {
    position: absolute;
    display: flex;
    align-items: center;
  }
  .brand__mark { background: var(--yellow); flex: none; }
  .brand__name {
    color: var(--green);
    font-family: "PT Sans Narrow", "Arial Narrow", sans-serif;
    font-weight: 700;
    text-transform: uppercase;
    line-height: 0.95;
  }
  .card--front .brand { left: 76px; top: 48px; gap: 16px; }
  .card--front .brand__mark { width: 96px; height: 96px; }
  .card--front .brand__name { font-size: 38px; }

  .card--back .brand { left: 52px; top: 40px; gap: 8px; }
  .card--back .brand__mark { width: 36px; height: 36px; }
  .card--back .brand__name { font-size: 15px; }

  .contact {
    position: absolute;
    right: 28px;
    text-align: right;
    color: var(--ink);
  }
  .contact::after {
    content: "";
    position: absolute;
    right: -17px;
    width: 9px;
  }
  .contact--person { top: 102px; }
  .contact--person::after { top: 4px; height: 24px; background: var(--green); }
  .contact__name {
    font-family: "PT Sans", Arial, sans-serif;
    font-weight: 700;
    font-size: 18px;
    line-height: 1.1;
  }
  .contact__role {
    font-weight: 700;
    font-size: 10.5px;
    color: var(--muted);
  }
  .contact--details { top: 146px; font-weight: 700; font-size: 10.5px; line-height: 1.25; }
  .contact--details::after { top: 0; height: 65px; background: var(--yellow); }
  .contact__address { margin-bottom: 9px; }
</style>
</head>
<body>
  <section class="card card--front">
    <div class="backdrop-shape" role="img" aria-label="Faint background area in brand tones"></div>
    <div class="brand">
      <span class="brand__mark"></span>
      <span class="brand__name">Wattlegrove<br>Campus<br>Lodgings</span>
    </div>
  </section>

  <section class="card card--back">
    <div class="backdrop-shape" role="img" aria-label="Faint background area in brand tones"></div>
    <div class="brand">
      <span class="brand__mark"></span>
      <span class="brand__name">Wattlegrove<br>Campus Lodgings</span>
    </div>
    <div class="contact contact--person">
      <p class="contact__name">Liam Hartley</p>
      <p class="contact__role">Manager</p>
    </div>
    <div class="contact contact--details">
      <p class="contact__address">18 Banksia Road Kelmore, Au&nbsp; 3140</p>
      <p class="contact__phone">917 555&nbsp; 0188&nbsp; EXT . 14</p>
      <p class="contact__email">stays@wattlegrovelodgings.com</p>
    </div>
  </section>
</body>
</html>
```